BOOK COVER: "The 5 Bold Rules Of Garden Harmony"

Hello!

This design contest is for a full book cover (front, back, spine) that will be printed via PressVolta (Thimble Foundry), as well as published as an ebook on Corvel Leafreader.

• When preparing this cover, please keep the requirements of PressVolta and Corvel Leafreader in mind. See the design brief below for format and resolution. I have also attached requirements for PressVolta as a separate file.

• The size of the book is A5. Please see attached PressVolta template for size.

• Please submit full book cover designs (front, back, spine) – just ONE image in flat form for each design. Feel free to upload multiple designs. Don’t upload multiple files of the same cover in 3D.

• The exact information to be included on the front, back and spine is outlined in the attached brief document.

• The chosen winner will need to provide full layered PSD or INDD files, plus high-resolution copies of any images used, plus font files.

• We may require minor edits to the chosen winners design before finalising payment.

If you have any questions, please ask in the comments.

Good luck!

*** PLEASE SEE ATTACHED DOCUMENT FOR FULL BRIEF! ***

Target Market(s)

Industry/Entity Type

Mortgage

Font styles to use
Serif
Sans Serif

Requirements
Must have
• *** PLEASE SEE ATTACHED DOCUMENT FOR FULL BRIEF! ***
Nice to have
Should not have

```html
<!DOCTYPE html>
<html lang="en">
<head>
<meta charset="utf-8">
<title>The 5 Bold Rules Of Garden Harmony – Full Cover</title>
<link rel="stylesheet" href="https://fonts.googleapis.com/css2?family=Oswald:wght@300;400;600;700&family=Bodoni+Moda:ital,wght@0,400;1,400&family=Open+Sans:ital,wght@0,400;0,700;1,400&display=swap">
<style>
  :root {
    --stage: #e4e6e5;
    --cover-green: #1f9a3e;
    --spine-green: #1b8f38;
    --lime: #8cc63f;
    --deep-green: #1a6e2c;
    --yellow: #f4ec1f;
    --quote-yellow: #d6e84a;
    --white: #ffffff;
    --paper: #f6f6f2;
    --ink: #3a3a3a;
    --photo-a: #b9a894;
    --photo-b: #5b6470;
  }
  * { box-sizing: border-box; margin: 0; padding: 0; }
  html, body { width: 1200px; height: 850px; overflow: hidden; }
  body {
    background: var(--stage);
    display: flex; align-items: center; justify-content: center;
    font-family: "Open Sans", Arial, sans-serif;
  }
  .full-cover { display: flex; width: 964px; height: 640px; box-shadow: 0 6px 24px rgba(0,0,0,.18); }

  /* Back cover */
  .back-cover {
    width: 452px; height: 100%; background: var(--cover-green);
    padding: 26px 22px 22px; color: var(--white); position: relative;
  }
  .back-headline {
    font-family: "Oswald", sans-serif; font-weight: 600; color: var(--yellow);
    font-size: 17.5px; line-height: 1.2; letter-spacing: .2px; margin-bottom: 14px;
  }
  .back-body { display: flex; gap: 12px; }
  .author-column { width: 146px; flex: none; }
  .author-photo {
    width: 146px; height: 168px;
    background: linear-gradient(160deg, var(--photo-a), var(--photo-b));
  }
  .author-bio {
    background: var(--paper); color: var(--ink);
    font-size: 7.6px; line-height: 1.42; padding: 9px 8px 8px; text-align: justify;
  }
  .author-bio p { margin-bottom: 8px; }
  .bio-site { font-weight: 700; font-size: 7.6px; margin-bottom: 6px; }
  .publisher-name {
    font-family: "Oswald", sans-serif; font-weight: 400; color: var(--deep-green);
    font-size: 12px; display: flex; align-items: center; gap: 5px;
  }
  .publisher-name::before { content: ""; width: 9px; height: 9px; background: var(--cover-green); }
  .pitch-column { flex: 1; font-size: 8.6px; line-height: 1.38; }
  .pitch-intro { margin-bottom: 6px; }
  .pitch-lead { font-weight: 700; font-size: 9.4px; margin-bottom: 4px; }
  .benefit-list { list-style: none; }
  .benefit-list li { position: relative; padding-left: 11px; margin-bottom: 5px; text-align: justify; }
  .benefit-list li::before { content: "➢"; position: absolute; left: 0; font-size: 7px; top: 1px; }
  .testimonial {
    font-style: italic; color: var(--quote-yellow); font-size: 8.4px; line-height: 1.36;
    text-align: justify; margin-top: 8px;
  }
  .testimonial cite { display: block; font-style: italic; margin-top: 2px; }

  /* Spine */
  .spine {
    width: 60px; height: 100%; background: var(--spine-green);
    display: flex; flex-direction: column; align-items: center; justify-content: space-between;
    padding: 26px 0 24px;
  }
  .spine-title, .spine-author {
    writing-mode: vertical-rl; font-family: "Oswald", sans-serif; font-size: 21px; letter-spacing: .4px;
  }
  .spine-title { color: var(--yellow); font-weight: 400; }
  .spine-mark { width: 16px; height: 16px; background: var(--lime); margin: 8px 0; }
  .spine-author { color: var(--white); font-weight: 400; }

  /* Front cover */
  .front-cover {
    width: 452px; height: 100%; background: var(--cover-green); position: relative; overflow: hidden;
  }
  .big-numeral {
    position: absolute; left: -18px; top: 0; font-family: "Bodoni Moda", serif;
    font-size: 470px; line-height: 1; color: var(--white);
  }
  .title-block { position: absolute; right: 32px; top: 120px; width: 300px; text-align: right; }
  .title-the {
    position: absolute; left: 6px; top: 22px; font-family: "Oswald", sans-serif;
    color: var(--white); font-size: 22px; font-weight: 400;
  }
  .title-accent {
    display: block; font-family: "Bodoni Moda", serif; font-style: italic; color: var(--yellow);
    font-size: 82px; line-height: 1; margin-right: 18px;
  }
  .title-line {
    display: block; font-family: "Oswald", sans-serif; font-weight: 400; color: var(--white);
    font-size: 64px; line-height: 1.06; letter-spacing: 1px;
  }
  .title-highlight {
    display: inline-block; background: var(--lime); color: var(--deep-green);
    padding: 0 14px; margin: 6px 0 4px; font-size: 60px;
  }
  .subtitle {
    position: absolute; right: 48px; top: 498px; width: 250px; text-align: right;
    font-family: "Oswald", sans-serif; font-weight: 600; color: var(--white);
    font-size: 9.5px; line-height: 1.3; letter-spacing: .3px;
  }
  .front-author {
    position: absolute; right: 92px; top: 534px; font-family: "Oswald", sans-serif;
    font-weight: 700; color: var(--yellow); font-size: 34px; letter-spacing: .5px;
  }
</style>
</head>
<body>
<main class="full-cover">

  <section class="back-cover">
    <h2 class="back-headline">STUCK AT WORK? FINANCIALLY STRESSED?<br>NO END TO YOUR MORTGAGE IN SIGHT?</h2>
    <div class="back-body">
      <div class="author-column">
        <div class="author-photo" role="img" aria-label="Portrait photograph of the author in a dark suit"></div>
        <div class="author-bio">
          <p>Owen Tarrant founded Meridian Homeloans to help home owners find a genuine low-cost home loan deal. Since then his business has grown into a network of local mortgage consultants who have organised over $2 billion in Home and Investment loans, with over 6,500 current client accounts. Most importantly, Owen practices what he preaches. Over a 7 year period from 2005, he went from having a $920,000 home loan to being mortgage free, while only paying the minimum repayments required. Owen's mission is to show you how he did it, so you can too.</p>
          <div class="bio-site">www.meridianhomeloans.com.au</div>
          <div class="publisher-name">Meridian Homeloans</div>
        </div>
      </div>
      <div class="pitch-column">
        <p class="pitch-intro">Learn how to get off the financial treadmill faster and finally start living life to the fullest!</p>
        <p class="pitch-lead">The 5 Bold Rules Of Garden Harmony will teach you:</p>
        <ul class="benefit-list">
          <li>Never to pay a cent more than necessary and exactly how to find a genuine low-cost home loan deal.</li>
          <li>Why most people will end up broke and the smart money tips you need to avoid becoming another statistic.</li>
          <li>“Good Debt” vs “Bad Debt” – and why most people think about this the wrong way.</li>
          <li>The millionaires trick to building wealth and financial security – that virtually anyone can do in almost any financial situation.</li>
          <li>Easily avoidable, but costly mistakes many home owners and investors make and how to avoid them.</li>
          <li>The Owen Tarrant true story: mortgage free in just 7 years and how you can too!</li>
          <li>Australians are working hard, trying to get ahead. But it’s not enough; most are failing because they don’t know how to get their finances working smart. Well it doesn’t have to be that way, because you’re about to discover the 5 bold rules to erasing your home loan fast – plus how to get smart with your money and secure your financial future once and for all!</li>
        </ul>
        <blockquote class="testimonial">“We wish to express our appreciation for the level of help and for the professional manner in which you gave it as a Mortgage Consultant. We are particularly impressed by your non-pushy, non-biased approach to your work; and also for your comprehensive knowledge of the banking sector and real estate industry.”
          <cite>-Gavin and Rose Pell, Tarrowvale QLD</cite>
        </blockquote>
      </div>
    </div>
  </section>

  <section class="spine">
    <span class="spine-title">THE 5 BOLD RULES OF GARDEN HARMONY</span>
    <span class="spine-mark"></span>
    <span class="spine-author">OWEN TARRANT</span>
  </section>

  <section class="front-cover">
    <span class="big-numeral" aria-hidden="true">5</span>
    <h1 class="title-block">
      <span class="title-the">THE</span>
      <span class="title-accent">Bold</span>
      <span class="title-line">RULES OF</span>
      <span class="title-line title-highlight">GARDEN</span>
      <span class="title-line">HARMONY</span>
    </h1>
    <p class="subtitle">REVEALED BY A MORTGAGE INDUSTRY INSIDER<br>WHO DID IT IN JUST 7 YEARS</p>
    <p class="front-author">OWEN TARRANT</p>
  </section>

</main>
</body>
</html>
```